Letterhead for paint manufacturing company

We need a letterhead for a paint manufacturing company called Corvane Industries Limited. We manufacture paint for construction companies as well as end consumers. We don't have a logo. Would like to see a design incorporating Pastel colours. We are based in Nigeria. Information to be included on the letterhead are:
Company name; Address: 12 plot C Adenuga Trading Estate, Ogba, Ikeja; Phone numbers: 08061723958, 08127490361

```html
<!DOCTYPE html>
<html lang="en">
<head>
<meta charset="utf-8">
<title>Corvane Industries Limited – Letterhead Concepts</title>
<link rel="stylesheet" href="https://fonts.googleapis.com/css2?family=Lato:wght@400&family=Josefin+Sans:wght@400&family=Source+Sans+3:wght@400&display=swap">
<style>
  :root{
    --backdrop:#e9e6e1;
    --paper:#ffffff;
    --lilac:#9a8cc7;
    --sage:#d6e2a4;
    --cream:#f1ecdf;
    --orchid:#b56fb4;
    --ink:#1c1c1c;
    --sky:#7d9fdc;
    --mint:#8fcb95;
    --lime:#d3e29a;
    --link-blue:#6f92d8;
  }
  *{margin:0;padding:0;box-sizing:border-box}
  html,body{width:1200px;height:649px;overflow:hidden;background:var(--backdrop)}
  .stage{position:relative;width:1200px;height:649px}
  .sheet{position:absolute;background:var(--paper);overflow:hidden;box-shadow:0 2px 10px rgba(0,0,0,.15)}
  .sheet svg.art{position:absolute;inset:0;width:100%;height:100%}

  /* Concept A – ellipse frame */
  .sheet--ellipse{left:153px;top:46px;width:393px;height:556px}
  .sheet--ellipse .company-name{
    position:absolute;right:17px;top:52px;
    font:400 15px/1 "Lato",sans-serif;color:var(--orchid);letter-spacing:.1px
  }
  .sheet--ellipse .contact-line{
    position:absolute;left:18px;top:523px;
    font:400 7.4px/1 "Josefin Sans",sans-serif;color:var(--ink);
    transform:rotate(-3.6deg);transform-origin:left center;
    display:flex;align-items:center;gap:5px;white-space:nowrap
  }
  .contact-line svg{width:7px;height:7px;flex:none}

  /* Concept B – corner waves */
  .sheet--waves{left:637px;top:43px;width:398px;height:565px}
  .sheet--waves .company-name{
    position:absolute;left:16px;top:14px;
    font:400 15px/1 "Source Sans 3",sans-serif;color:var(--ink)
  }
  .sheet--waves .contact-block{
    position:absolute;right:10px;top:533px;text-align:right;
    font:400 7px/1 "Source Sans 3",sans-serif;color:var(--link-blue)
  }
  .contact-block p{display:flex;justify-content:flex-end;align-items:center;gap:4px;margin-bottom:5px}
  .contact-block svg{width:7px;height:7px;flex:none}
</style>
</head>
<body>
<main class="stage">

  <section class="sheet sheet--ellipse" aria-label="Letterhead concept with lilac and sage ellipse frame">
    <svg class="art" viewBox="0 0 393 556" preserveAspectRatio="none" aria-hidden="true">
      <path d="M0 0H393V22C250 16 90 45 0 152Z" fill="var(--cream)"/>
      <path d="M0 0H235C140 10 45 38 0 88Z" fill="var(--sage)"/>
      <path d="M92 40C200 10 320 0 393 0V56C300 24 200 22 92 40Z" fill="var(--lilac)"/>
      <path d="M90 488C240 482 340 455 393 414V462C300 486 200 492 90 488Z" fill="var(--cream)"/>
      <path d="M0 455C80 485 200 494 330 490C220 502 90 506 0 508Z" fill="var(--lilac)"/>
      <path d="M0 556V502C150 502 300 486 393 460V556Z" fill="var(--sage)"/>
    </svg>
    <h1 class="company-name">Corvane Industries Limited</h1>
    <p class="contact-line">
      <svg viewBox="0 0 10 10"><path d="M5 0.5A3.3 3.3 0 0 0 1.7 3.8C1.7 6.3 5 9.5 5 9.5S8.3 6.3 8.3 3.8A3.3 3.3 0 0 0 5 0.5ZM5 5.1A1.3 1.3 0 1 1 5 2.5A1.3 1.3 0 0 1 5 5.1Z" fill="var(--ink)"/></svg>
      <span>12 plot C Adenuga Trading Estate, Ogba, Ikeja</span>
      <svg viewBox="0 0 10 10"><circle cx="5" cy="5" r="4.3" fill="none" stroke="var(--ink)" stroke-width="1"/><path d="M3.4 2.8L4.3 3.9L3.9 4.6C4.3 5.3 4.7 5.7 5.4 6.1L6.1 5.7L7.2 6.6L6.6 7.3C4.8 7.1 2.9 5.2 2.7 3.4Z" fill="var(--ink)"/></svg>
      <span>08061723958, 08127490361</span>
    </p>
  </section>

  <section class="sheet sheet--waves" aria-label="Letterhead concept with pastel corner waves">
    <svg class="art" viewBox="0 0 398 565" preserveAspectRatio="none" aria-hidden="true">
      <path d="M232 62C290 52 320 8 398 2V14C330 20 300 62 232 62Z" fill="var(--sky)"/>
      <path d="M262 64C310 55 335 20 398 14V30C340 32 320 62 262 64Z" fill="var(--mint)"/>
      <path d="M250 70C320 68 340 35 398 36V40C345 40 325 70 250 70Z" fill="var(--lime)"/>
      <path d="M0 505C40 525 100 498 140 497C120 502 70 522 0 520Z" fill="var(--lime)"/>
      <path d="M0 525C60 535 110 496 165 505C110 506 60 548 0 545Z" fill="var(--mint)"/>
      <path d="M0 548C80 560 110 500 165 505C115 510 90 565 40 565H0Z" fill="var(--sky)"/>
    </svg>
    <h1 class="company-name">Corvane Industries Limited</h1>
    <div class="contact-block">
      <p>
        <svg viewBox="0 0 10 10"><path d="M5 0.5A3.3 3.3 0 0 0 1.7 3.8C1.7 6.3 5 9.5 5 9.5S8.3 6.3 8.3 3.8A3.3 3.3 0 0 0 5 0.5ZM5 5.1A1.3 1.3 0 1 1 5 2.5A1.3 1.3 0 0 1 5 5.1Z" fill="var(--ink)"/></svg>
        <span>12 plot C Adenuga Trading Estate, Ogba, Ikeja</span>
      </p>
      <p>
        <svg viewBox="0 0 10 10"><circle cx="5" cy="5" r="4.3" fill="none" stroke="var(--ink)" stroke-width="1"/><path d="M3.4 2.8L4.3 3.9L3.9 4.6C4.3 5.3 4.7 5.7 5.4 6.1L6.1 5.7L7.2 6.6L6.6 7.3C4.8 7.1 2.9 5.2 2.7 3.4Z" fill="var(--ink)"/></svg>
        <span>08061723958, 08127490361</span>
      </p>
    </div>
  </section>

</main>
</body>
</html>
```